Special release wine label

Marrow Creek Vineyards is a small premium wine producer in the Barossa - South Australia. We are a five star rated winery, producing exceptional wines true to variety, region and house style. We have a very special parcel of wine that we wish to release as an exclusive wine. Visit www.marrowcreekvineyards.com.au for further feel.

The wine will be called Marrow Creek Vineyards, 2012, The Quiet Harvest Shiraz - Cabernet.

The wine can be bottled in either a burgundy or Bordeaux shaped bottle

Industry/Entity Type

House

```html
<!DOCTYPE html>
<html lang="en">
<head>
<meta charset="utf-8">
<title>Marrow Creek Vineyards – The Quiet Harvest Shiraz Cabernet label</title>
<link rel="stylesheet" href="https://fonts.googleapis.com/css2?family=Cinzel:wght@500;600&family=Libre+Bodoni:ital,wght@0,400;0,500;1,400&display=swap">
<style>
  :root {
    --stage: #ece6db;
    --paper: #ffffff;
    --ink: #5b2a36;
    --ink-soft: #8a6068;
    --rule: #b79ea3;
    --art-top: #e9e1e2;
    --art-bottom: #c9b3b7;
  }
  * { box-sizing: border-box; margin: 0; padding: 0; }
  html, body {
    width: 1200px; height: 900px; overflow: hidden;
    background: var(--stage);
  }
  .canvas {
    width: 1200px; height: 900px;
    display: flex; align-items: center; justify-content: center;
  }
  .label {
    width: 360px; height: 830px;
    background: var(--paper);
    color: var(--ink);
    padding: 26px 26px 20px;
    display: flex; flex-direction: column;
    box-shadow: 0 2px 10px rgba(60, 40, 30, 0.12);
  }
  .brand {
    font-family: "Cinzel", serif;
    font-weight: 600;
    font-size: 37px;
    letter-spacing: 2px;
    line-height: 1;
    padding-bottom: 16px;
    border-bottom: 1px solid var(--rule);
    white-space: nowrap;
  }
  .brand-row {
    display: flex;
    border-bottom: 1px solid var(--rule);
    font-family: "Cinzel", serif;
    font-weight: 500;
    font-size: 19px;
    letter-spacing: 3px;
  }
  .brand-row .sub { padding: 12px 22px 10px 2px; border-right: 1px solid var(--rule); }
  .brand-row .vintage { padding: 12px 0 10px 22px; font-family: "Libre Bodoni", serif; letter-spacing: 2px; }
  .homestead-art {
    margin-top: 30px;
    height: 230px;
    background: linear-gradient(180deg, var(--art-top), var(--art-bottom));
  }
  .art-rule { margin-top: 22px; border-top: 1px solid var(--rule); }
  .wine-name {
    margin-top: 30px;
    font-family: "Libre Bodoni", serif;
    font-style: italic;
    font-size: 30px;
    line-height: 1;
  }
  .varietal {
    margin-top: 20px;
    font-family: "Libre Bodoni", serif;
    font-size: 52px;
    line-height: 1.02;
    letter-spacing: 0.5px;
  }
  .story {
    margin-top: 24px;
    font-family: "Libre Bodoni", serif;
    font-variant: small-caps;
    font-weight: 500;
    font-size: 12.5px;
    line-height: 2.05;
  }
  .footer {
    margin-top: auto;
    border-top: 1px solid var(--rule);
    padding-top: 9px;
    display: flex; justify-content: space-between;
    font-family: "Libre Bodoni", serif;
    font-size: 9px;
    letter-spacing: 3px;
    color: var(--ink-soft);
    text-transform: uppercase;
  }
</style>
</head>
<body>
  <main class="canvas">
    <article class="label">
      <h1 class="brand">Marrow Creek</h1>
      <div class="brand-row">
        <span class="sub">Vineyards</span>
        <span class="vintage">2012</span>
      </div>
      <div class="homestead-art" role="img" aria-label="Engraved-style sketch of the winery homestead framed by tall palm trees and a cypress"></div>
      <div class="art-rule"></div>
      <p class="wine-name">The Quiet Harvest</p>
      <h2 class="varietal">SHIRAZ<br>CABERNET</h2>
      <p class="story">Marrow Creek Vineyards was established by the Harlow Family in 1997. Marrow Creek Vineyards is a family owned and operated winery; with Anna and Tom Harlow building Marrow Creek into a premium winery specialising in regional wines of distinctive quality.</p>
      <div class="footer">
        <span>South Australia</span>
        <span>750 ml</span>
      </div>
    </article>
  </main>
</body>
</html>
```